50 Page Catalog Full Redesign New Look

We are looking for a redesign of our Catalog,

We are looking for a modern redesign of our Catalog, with our new logo most of the products will be the same with some new products as well.
Please use colors in the new logo attached
Attached is our current design please see this for what product will go in the catulog
Updates

Designs look the same

Target Market(s)

Automotive

Font styles to use
Other font styles liked:
• Our Font is outfit

Colors

Designer to choose colors to be used in the design.

```html
<!DOCTYPE html>
<html lang="en">
<head>
<meta charset="utf-8">
<title>Who We Are — Corvana</title>
<link rel="stylesheet" href="https://fonts.googleapis.com/css2?family=Outfit:wght@300;400;800&display=swap">
<style>
  :root {
    --brand-dark: #0563a0;
    --brand-light: #1a91d1;
    --ink: #1a1a1a;
    --paper: #ffffff;
    --gap: #ffffff;
  }
  html, body {
    margin: 0;
    padding: 0;
    overflow: hidden;
    background: var(--paper);
  }
  .page {
    position: relative;
    width: 942px;
    height: 1200px;
    overflow: hidden;
    background: var(--paper);
    font-family: "Outfit", sans-serif;
    color: var(--ink);
  }
  .page-title {
    position: absolute;
    left: 118px;
    top: 172px;
    margin: 0;
    font-size: 50px;
    font-weight: 800;
    letter-spacing: -2.5px;
    color: var(--brand-dark);
    line-height: 1;
  }
  .intro {
    position: absolute;
    left: 119px;
    top: 244px;
    margin: 0;
    font-size: 18.6px;
    font-weight: 400;
    line-height: 24.1px;
  }
  .intro span { display: block; white-space: nowrap; }
  .values-wheel {
    position: absolute;
    left: 0;
    top: 0;
    width: 942px;
    height: 1200px;
  }
  .segment-dark { fill: var(--brand-dark); }
  .segment-light { fill: var(--brand-light); }
  .segment-gap { stroke: var(--gap); stroke-width: 11; }
  .segment-label {
    font-family: "Outfit", sans-serif;
    font-weight: 800;
    font-size: 20px;
    fill: #ffffff;
    letter-spacing: -0.5px;
  }
  .portrait {
    position: absolute;
    left: 207px;
    top: 630px;
    width: 280px;
    height: 455px;
    border-radius: 120px 120px 0 0;
    background: linear-gradient(180deg, #d9d4cf 0%, #e9e9ea 28%, #1f2a40 55%, #18223a 100%);
  }
  .quote {
    position: absolute;
    left: 556px;
    top: 897px;
    width: 342px;
    margin: 0;
    text-align: center;
    font-size: 22px;
    font-weight: 300;
    line-height: 22.6px;
  }
  .quote-author { display: block; }
</style>
</head>
<body>
<main class="page">
  <h1 class="page-title">WHO WE ARE</h1>
  <p class="intro">
    <span>For over three decades, Corvana has provided complete merchandise solutions</span>
    <span>for an ever- increasing number of Australian corporations and businesses.</span>
    <span>During this time, our already vast range has grown exponentially and our</span>
    <span>systems have become increasingly more streamlined to cope with the sheer</span>
    <span>volume.</span>
    <span>Our enviable reputation is built on experience, innovation and economies of</span>
    <span>scale that come with being a major wholesaler in Australia.</span>
    <span>We pride ourselves on our accountability, efficiency, consistency, instant</span>
    <span>reporting and above all, the ability to see things from your point of view.</span>
    <span>We love to strategise with you to make sure what we supply will achieve the</span>
    <span>desired outcome. Every day we see companies giving away merchandise</span>
    <span>aimlessly and our mission is to supply you with a product that will suit your</span>
    <span>criteria.</span>
  </p>

  <svg class="values-wheel" viewBox="0 0 942 1200" aria-label="Our values: care, speed, satisfaction, enjoyment">
    <defs>
      <path id="label-arc" d="M 118 812 A 212 212 0 0 1 542 812"/>
    </defs>
    <path class="segment-dark" d="M 53 812 A 277 277 0 0 1 134.1 616.1 L 231 713 A 140 140 0 0 0 190 812 Z"/>
    <path class="segment-light" d="M 134.1 616.1 A 277 277 0 0 1 330 535 L 330 672 A 140 140 0 0 0 231 713 Z"/>
    <path class="segment-dark" d="M 330 535 A 277 277 0 0 1 525.9 616.1 L 429 713 A 140 140 0 0 0 330 672 Z"/>
    <path class="segment-light" d="M 525.9 616.1 A 277 277 0 0 1 607 812 L 470 812 A 140 140 0 0 0 429 713 Z"/>
    <line class="segment-gap" x1="231" y1="713" x2="128" y2="610"/>
    <line class="segment-gap" x1="330" y1="672" x2="330" y2="528"/>
    <line class="segment-gap" x1="429" y1="713" x2="532" y2="610"/>
    <text class="segment-label" text-anchor="middle"><textPath href="#label-arc" startOffset="12.5%">CARE</textPath></text>
    <text class="segment-label" text-anchor="middle"><textPath href="#label-arc" startOffset="37.5%">SPEED</textPath></text>
    <text class="segment-label" text-anchor="middle"><textPath href="#label-arc" startOffset="62.5%">SATISFACTION</textPath></text>
    <text class="segment-label" text-anchor="middle"><textPath href="#label-arc" startOffset="87.5%">ENJOYMENT</textPath></text>
  </svg>

  <div class="portrait" role="img" aria-label="Photo of a smiling businessman in a navy blazer and white shirt holding a takeaway coffee cup"></div>

  <p class="quote">“A man who stops advertising to save money is like a man who stops a clock to save time.” <span class="quote-author">Walter Brandt</span></p>
</main>
</body>
</html>
```